Brightway Haul & Repair Services, are a company that offers a 'one stop shop' pre-move clean up a

I have already selected a logo which I would like on the front of the business cards along with phone numbers, web address and email which are:
0419574302
www.brightwayhaul.com.au
brightwayhaulrepair@mailbox.example

On the back of the card I would like to list some of the types of service we offer (clean - move - repairs/maintenance) which are:
CLEAN - windows, gutters, solar panels, driveways/paths, carpets.
MOVE - Small/medium size house/office moves, large item pick-up & delivery, yard clean-up and removal.
General maintenance and repairs.

I would like the blue logo on a gray background.

Thanks

```html
<!DOCTYPE html>
<html lang="en">
<head>
<meta charset="utf-8">
<title>Brightway Haul &amp; Repair Services – Business Card</title>
<link href="https://fonts.googleapis.com/css2?family=Saira:wght@600&family=Arimo:wght@400;700&display=swap" rel="stylesheet">
<style>
  :root {
    --canvas: #000000;
    --card-grey: #e3e5e9;
    --card-grey-light: #f2f3f5;
    --brand-blue: #1f6fc1;
    --ink: #1c1c1c;
    --rule: #b9b9b9;
    --card-white: #ffffff;
    --card-edge: #9a9a9a;
  }
  * { margin: 0; padding: 0; box-sizing: border-box; }
  html, body {
    width: 1200px; height: 300px; overflow: hidden;
    background: var(--canvas);
  }
  .canvas { position: relative; width: 1200px; height: 300px; }

  .card { position: absolute; top: 24px; width: 422px; height: 251px; }

  /* Front */
  .card--front {
    left: 196px;
    background: linear-gradient(160deg, var(--card-grey-light) 0%, var(--card-grey) 45%, var(--card-grey-light) 100%);
    text-align: center;
  }
  .card__sheen { position: absolute; inset: 0; }
  .brand-name {
    position: absolute; left: 0; right: 0; top: 66px;
    font-family: "Saira", sans-serif; font-weight: 600;
    font-size: 31px; line-height: 36px;
    color: var(--brand-blue);
  }
  .contact { position: absolute; left: 0; right: 0; top: 168px; }
  .contact__phone {
    font-family: "Saira", sans-serif; font-weight: 600;
    font-size: 29px; line-height: 34px; letter-spacing: 1px;
    color: var(--brand-blue);
  }
  .contact__web {
    margin-top: 4px;
    font-family: "Arimo", sans-serif; font-weight: 700;
    font-size: 15px; line-height: 17px; color: var(--ink);
  }
  .contact__email {
    font-family: "Arimo", sans-serif; font-weight: 400;
    font-size: 15px; line-height: 17px; color: var(--ink);
  }

  /* Back */
  .card--back {
    left: 642px; top: 23px; width: 421px; height: 252px;
    background: var(--card-white);
    border: 1px solid var(--card-edge);
  }
  .write-line {
    position: absolute; left: 26px; width: 370px; height: 1px;
    background: var(--rule);
  }
  .write-line--first { top: 80px; }
  .write-line--second { top: 125px; }
  .services {
    position: absolute; left: 10px; right: 10px; top: 144px;
    font-family: "Arimo", sans-serif; font-size: 11.5px; line-height: 17.5px;
    color: var(--ink); text-align: center; list-style: none;
  }
</style>
</head>
<body>
<main class="canvas">
  <section class="card card--front" aria-label="Business card front">
    <svg class="card__sheen" width="422" height="251" viewBox="0 0 422 251" aria-hidden="true">
      <path d="M0 62 L250 0 L300 0 L0 80 Z" fill="#ffffff" opacity="0.55"/>
      <path d="M0 88 L300 8 L310 8 L0 94 Z" fill="#ffffff" opacity="0.6"/>
      <path d="M350 120 L422 72 L422 90 L372 122 Z" fill="#ffffff" opacity="0.5"/>
    </svg>
    <h1 class="brand-name">Brightway Haul<br>&amp; Repair Services</h1>
    <div class="contact">
      <p class="contact__phone">0419 574 302</p>
      <p class="contact__web">www.brightwayhaul.com.au</p>
      <p class="contact__email">brightwayhaulrepair@mailbox.example</p>
    </div>
  </section>

  <section class="card card--back" aria-label="Business card back">
    <div class="write-line write-line--first"></div>
    <div class="write-line write-line--second"></div>
    <ul class="services">
      <li>CLEAN - windows, gutters, solar panels,driveways/paths, carpets.</li>
      <li>MOVE - Small/medium size house/office moves, large item pick-up<br>&amp; delivery, yard clean-up and removal.</li>
      <li>GENERAL MAINTENANCE AND REPAIRS.</li>
    </ul>
  </section>
</main>
</body>
</html>
```